Cultured Basics Website Design

We need a modern, elegant website for a nutritional product called "Cultured Basics" which is based on the diets of people living in Longevity Hot Spots. In Longevity Hot Spots people live uncommonly longer and healthier lives. Most of these Hot Spots are in exotic locations around the world. I have attached several images taken from the Hot Spot in Costa Rica, along with our Logo and the text for the entire website. It is not necessary to use/include all of the text, we can add and adjust that later. For now, we need the design for the home page and template for interior pages. You do not have to use the images we provide, we can purchase additional images if needed. "Final selection should include Adobe Muse template file and all supporting graphics in editable formats (PhotoShop, Illustrator, etc)" We have posted several projects on Sketch Harbor and have accepted in every case. We look forward to seeing your design for our website. Thanks!
We like the look of these websites as an example. You have to press "Preview" (which is located on the right) to see the website.
https://www.pagebloomer.com/websites/templates/drift
https://www.pagebloomer.com/websites/templates/marlow
35-60 80% female, 20% male
Product
1 page

```html
<!DOCTYPE html>
<html lang="en">
<head>
<meta charset="utf-8">
<title>Cultured Basics — Naturally Enhanced Superfoods</title>
<link href="https://fonts.googleapis.com/css2?family=Josefin+Sans:wght@300;400;600&family=Open+Sans:wght@400;600&display=swap" rel="stylesheet">
<style>
:root{
  --green:#4e8f2f;
  --green-bright:#5aa63a;
  --green-dark:#3f7a24;
  --ink:#333;
  --muted:#555;
  --line:#d9d9d9;
  --footer:#1c1f1d;
  --star:#e39b2b;
  --white:#fff;
}
*{box-sizing:border-box;margin:0;padding:0}
html,body{width:1200px;height:3147px;overflow:hidden}
body{position:relative;background:var(--white);font-family:"Open Sans",sans-serif;color:var(--ink)}
.abs{position:absolute}
.heading{font-family:"Josefin Sans",sans-serif;font-weight:300;color:#222;text-align:center}

/* header */
.site-header{position:absolute;top:0;left:0;width:1200px;height:122px;background:var(--white);border-top:4px solid var(--green)}
.brand{position:absolute;left:98px;top:26px;display:flex;align-items:center;gap:10px}
.brand-dot{width:50px;height:50px;border-radius:50%;background:var(--green-bright)}
.brand-name{font-family:"Josefin Sans",sans-serif;font-weight:600;font-size:32px;color:var(--green);line-height:1}
.brand-tag{position:absolute;left:160px;top:84px;font-size:9px;color:#666}
.main-nav{position:absolute;left:430px;top:0;height:118px;display:flex;align-items:center;font-size:13px;color:#222}
.main-nav a{color:inherit;text-decoration:none;margin-right:36px}
.main-nav .active{background:var(--green);color:#fff;height:118px;display:flex;align-items:center;padding:0 20px;margin-right:38px}
.nav-search{position:absolute;left:1088px;top:50px}

/* hero */
.hero{position:absolute;top:122px;left:0;width:1200px;height:670px;overflow:hidden}
.hero-photo{position:absolute;inset:0;background:linear-gradient(180deg,#7b8a8c 0%,#5f7171 30%,#4d5f52 55%,#6a6a52 75%,#8a6f58 100%)}
.hero-title{position:absolute;top:170px;width:1200px;text-align:center;font-family:"Josefin Sans",sans-serif;font-weight:300;font-size:44px;color:#fff}
.hero-text{position:absolute;top:240px;left:215px;width:770px;text-align:center;font-size:16px;line-height:31px;color:#fff}
.hero-dots{position:absolute;top:352px;left:0;width:1200px;display:flex;justify-content:center;gap:14px}
.hero-dots span{width:20px;height:20px;border-radius:50%;border:2px solid #fff}
.hero-dots span.on{background:var(--green-bright)}
.hero-curve{position:absolute;left:0;bottom:0}

/* welcome */
.welcome-title{position:absolute;top:780px;width:1200px;font-size:28px}
.welcome-text{position:absolute;top:818px;left:128px;width:944px;text-align:center;font-size:12px;line-height:25px;color:var(--muted)}
.welcome-text a,.read-more{color:var(--green);text-decoration:underline}
.feature{position:absolute;top:950px;width:240px;text-align:center}
.feature-ring{width:134px;height:134px;margin:0 auto;border:2px solid var(--green);border-radius:50%;padding:8px}
.feature-icon{width:114px;height:114px;border-radius:50%;background:var(--green);display:flex;align-items:center;justify-content:center}
.feature-title{margin-top:20px;font-family:"Josefin Sans",sans-serif;font-size:16px;color:var(--green)}
.feature-text{margin-top:8px;font-size:11.5px;line-height:21px;color:var(--muted)}
.feature .read-more{display:block;margin-top:6px;font-size:12px}

/* story */
.story{position:absolute;top:1259px;left:0;width:1200px;height:427px}
.story-photo{position:absolute;inset:0;background:linear-gradient(90deg,#6f7b3f 0%,#4f7a32 25%,#c9b9a0 45%,#8a8c62 60%,#b9a37e 100%)}
.story-panel{position:absolute;left:734px;top:0;width:367px;height:427px;background:rgba(245,240,232,.88);text-align:center;padding:34px 40px}
.story-panel h2{font-family:"Josefin Sans",sans-serif;font-weight:300;font-size:28px;color:#222;margin-bottom:14px}
.story-panel p{font-size:12px;line-height:26px;color:#444}
.story-panel a{display:block;margin-top:4px;font-size:12px;color:var(--green);text-decoration:none}

/* products */
.products-title{position:absolute;top:1720px;width:1200px;font-size:28px}
.products-text{position:absolute;top:1758px;left:140px;width:920px;text-align:center;font-size:12px;line-height:26px;color:var(--muted)}
.product-card{position:absolute;width:232px;height:382px;border:1px solid var(--line);background:#fff;text-align:center}
.product-name{height:42px;background:var(--green);color:#fff;font-family:"Josefin Sans",sans-serif;font-size:15px;line-height:44px}
.product-photo{width:190px;height:170px;margin:14px auto 0;border-radius:6px}
.product-text{margin-top:18px;font-size:11px;line-height:21px;color:var(--muted);padding:0 20px}
.product-rating{margin-top:8px;font-size:10.5px;color:#444}
.product-rating b{color:var(--star);font-size:13px;letter-spacing:1px;font-weight:400}
.order-btn{display:inline-block;margin-top:12px;width:130px;height:38px;line-height:38px;background:var(--green);color:#fff;font-size:13px;border:1px solid var(--green-dark)}

/* footer */
.site-footer{position:absolute;top:2677px;left:0;width:1200px;height:411px;background:var(--footer);color:#ddd}
.footer-brand{position:absolute;left:98px;top:44px;display:flex;align-items:center;gap:10px}
.footer-brand .brand-dot{width:44px;height:44px;background:#fff}
.footer-brand .brand-name{color:#fff;font-size:28px}
.social{position:absolute;left:934px;top:50px;display:flex;gap:7px}
.social span{width:28px;height:28px;border:1.5px solid #ddd;border-radius:50%}
.footer-col h3{font-family:"Josefin Sans",sans-serif;font-weight:300;font-size:19px;color:#fff;margin-bottom:18px}
.quick-links{position:absolute;left:98px;top:165px}
.quick-links li{list-style:none;font-size:12px;line-height:25.6px;color:#eee}
.contact{position:absolute;left:342px;top:165px;font-size:12.5px;color:#eee}
.contact-row{display:flex;gap:12px;margin-bottom:14px;line-height:22px}
.contact-form{position:absolute;left:638px;top:155px;width:463px}
.field{position:absolute;height:36px;border:1px solid #ccc;border-radius:4px;font-size:11px;color:#eee;padding:9px 12px}
.send-btn{position:absolute;left:0;top:170px;width:120px;height:40px;background:var(--green);border:2px solid #ccc;color:#fff;font-size:11px;line-height:36px;text-align:center}
.footer-bar{position:absolute;top:3088px;left:0;width:1200px;height:59px;background:var(--green);color:#fff;font-size:12px;line-height:59px;text-align:center}
</style>
</head>
<body>

<header class="site-header">
  <div class="brand"><span class="brand-dot"></span><span class="brand-name">Cultured Basics</span></div>
  <div class="brand-tag">Naturally Enhanced Superfoods</div>
  <nav class="main-nav">
    <a class="active">Home</a><a>Story</a><a>Product</a><a>How to take Cultured Basics</a><a>FAQ</a><a>Science Advisory Board</a>
  </nav>
  <svg class="nav-search" width="16" height="16" viewBox="0 0 16 16"><circle cx="6.5" cy="6.5" r="4.8" fill="none" stroke="#4e8f2f" stroke-width="2"/><line x1="10" y1="10" x2="14.5" y2="14.5" stroke="#4e8f2f" stroke-width="2.4"/></svg>
</header>

<section class="hero">
  <div class="hero-photo" role="img" aria-label="Tropical bay with forested hills, palm trees and a beach in a longevity hot spot"></div>
  <h1 class="hero-title">Naturally Enhanced Superfoods</h1>
  <p class="hero-text">The healthiest people on earth eat consume a diet that is quite different from ours including a great deal of fermented foods, a variety of superfoods and probiotics. Cultured Basics helps bridge the gap between their diet and ours...</p>
  <div class="hero-dots"><span class="on"></span><span></span><span></span></div>
  <svg class="hero-curve" width="1200" height="190" viewBox="0 0 1200 190">
    <path d="M0,45 Q600,150 1200,40 L1200,190 L0,190Z" fill="#fff"/>
    <path d="M0,60 Q600,168 1200,55 Q600,230 0,60Z" fill="#4e9a30"/>
  </svg>
</section>

<h2 class="heading welcome-title">Welcome to Cultured Basics</h2>
<p class="welcome-text">For thousands of years in remote areas scattered across the globe, a handful of cultures have mastered the art of living well. In these extraordinary places, diseases are rare, sickness is infrequent and life expectancies of 90 to 100 plus years are common. These are commonly referred to as Longevity Hot Spots. While researching the diets of these remarkably healthy people, we made an amazing discovery that has a profound impact on health: People in Longevity Hot Spots consume fermented foods on a daily basis. Fermentation is a process our ancestors... <a>Read More +</a></p>

<div class="feature" style="left:86px">
  <div class="feature-ring"><div class="feature-icon"><svg width="56" height="56" viewBox="0 0 56 56"><path d="M28 30 C20 26 18 16 26 10 C30 18 32 24 28 30Z M30 30 C36 24 42 24 46 26 C42 32 36 33 30 30Z" fill="#fff"/><path d="M8 40 Q20 34 30 40 L44 36 Q48 36 46 40 L32 48 L8 48Z" fill="#fff"/></svg></div></div>
  <div class="feature-title">Vegan</div>
  <p class="feature-text">Nemo enim ipsam voluptatem quia voluptas sit aspernatur aut odit aut fugit, sed quia voluptatem sequi nesc...</p>
  <a class="read-more">Read More +</a>
</div>
<div class="feature" style="left:348px">
  <div class="feature-ring"><div class="feature-icon"><svg width="56" height="56" viewBox="0 0 56 56"><ellipse cx="28" cy="30" rx="20" ry="16" fill="#fff"/><path d="M22 16 Q30 28 26 46" stroke="#4e8f2f" stroke-width="3" fill="none"/></svg></div></div>
  <div class="feature-title">Non Dairy</div>
  <p class="feature-text">Nemo enim ipsam voluptatem quia voluptas sit aspernatur aut odit aut fugit, sed quia voluptatem sequi nesc...</p>
  <a class="read-more">Read More +</a>
</div>
<div class="feature" style="left:610px">
  <div class="feature-ring"><div class="feature-icon"><svg width="56" height="56" viewBox="0 0 56 56"><rect x="10" y="26" width="9" height="20" fill="#fff"/><path d="M22 26 L30 10 Q35 10 34 18 L33 24 L44 24 Q48 25 47 30 L44 44 Q43 46 40 46 L22 46Z" fill="#fff"/></svg></div></div>
  <div class="feature-title">No Fillers</div>
  <p class="feature-text">Nemo enim ipsam voluptatem quia voluptas sit aspernatur aut odit aut fugit, sed quia voluptatem sequi nesc...</p>
  <a class="read-more">Read More +</a>
</div>
<div class="feature" style="left:872px">
  <div class="feature-ring"><div class="feature-icon"><svg width="56" height="56" viewBox="0 0 56 56"><path d="M28 30 C20 26 18 16 26 10 C30 18 32 24 28 30Z M30 30 C36 24 42 24 46 26 C42 32 36 33 30 30Z" fill="#fff"/><path d="M8 40 Q20 34 30 40 L44 36 Q48 36 46 40 L32 48 L8 48Z" fill="#fff"/></svg></div></div>
  <div class="feature-title">No Trans Fat</div>
  <p class="feature-text">Nemo enim ipsam voluptatem quia voluptas sit aspernatur aut odit aut fugit, sed quia voluptatem sequi nesc...</p>
  <a class="read-more">Read More +</a>
</div>

<section class="story">
  <div class="story-photo" role="img" aria-label="A smiling woman in a sun hat beside an elderly local man in a leafy garden"></div>
  <div class="story-panel">
    <h2>Our Story</h2>
    <p>Cultured Basics Story - Need to tweak the part about blueprint for life and sales figures. While on a business trip to Costa Rica in 2004, lifelong entrepreneur Daniel Reyes discovered a small village on the Nicoyan Peninsula where there are no hospitals and obesity, cancer and cardiovascular disease are virtually non existent. In this village of Nosara, people live healthy, vital lives well into their...</p>
    <a>Click Read More Information</a>
  </div>
</section>

<h2 class="heading products-title">Our Products</h2>
<p class="products-text">Cultured Basics contains high performance, therapeutic whole foods from organic ingredients while delivering nutrients as nature intended. Simply put, Cultured Basics utilizes fermented superfoods to fill the gaps in your current diet.</p>

<div class="product-card" style="left:98px;top:1834px"><div class="product-name">Organic Apple</div><div class="product-photo" role="img" aria-label="Red apples" style="background:radial-gradient(circle,#c8262a 0%,#a31e22 45%,#fff 75%)"></div><p class="product-text">Totam rem aperiam, eaque ipsa quae veritatis et quasi architecto...</p><div class="product-rating"><b>★★★★☆</b> 120 Reviews</div><span class="order-btn">Order Now</span></div>
<div class="product-card" style="left:356px;top:1834px"><div class="product-name">Organic Oat Bran</div><div class="product-photo" role="img" aria-label="Oat bran and oat stalks" style="background:radial-gradient(circle,#d8c08e 0%,#c4a66a 45%,#fff 75%)"></div><p class="product-text">Totam rem aperiam, eaque ipsa quae veritatis et quasi architecto...</p><div class="product-rating"><b>★★★★☆</b> 120 Reviews</div><span class="order-btn">Order Now</span></div>
<div class="product-card" style="left:612px;top:1834px"><div class="product-name">Organic Ginger Root Extract</div><div class="product-photo" role="img" aria-label="Ginger root and powder on a green plate" style="background:radial-gradient(circle,#c9a46a 0%,#8ba447 55%,#fff 80%)"></div><p class="product-text">Totam rem aperiam, eaque ipsa quae veritatis et quasi architecto...</p><div class="product-rating"><b>★★★★☆</b> 120 Reviews</div><span class="order-btn">Order Now</span></div>
<div class="product-card" style="left:868px;top:1834px"><div class="product-name">Black Garlic</div><div class="product-photo" role="img" aria-label="Blueberries" style="background:radial-gradient(circle,#2d4fa0 0%,#1d3478 45%,#fff 75%)"></div><p class="product-text">Totam rem aperiam, eaque ipsa quae veritatis et quasi architecto...</p><div class="product-rating"><b>★★★★☆</b> 120 Reviews</div><span class="order-btn">Order Now</span></div>

<div class="product-card" style="left:98px;top:2246px"><div class="product-name">Black Garlic</div><div class="product-photo" role="img" aria-label="Halved bulbs of black garlic" style="background:radial-gradient(circle,#3a2e26 0%,#8a7a68 50%,#fff 78%)"></div><p class="product-text">Totam rem aperiam, eaque ipsa quae veritatis et quasi architecto...</p><div class="product-rating"><b>★★★★☆</b> 120 Reviews</div><span class="order-btn">Order Now</span></div>
<div class="product-card" style="left:356px;top:2246px"><div class="product-name">Organic Broccoli</div><div class="product-photo" role="img" aria-label="Fresh broccoli" style="background:radial-gradient(circle,#4f8a2a 0%,#6ea23c 45%,#fff 75%)"></div><p class="product-text">Totam rem aperiam, eaque ipsa quae veritatis et quasi architecto...</p><div class="product-rating"><b>★★★★☆</b> 120 Reviews</div><span class="order-btn">Order Now</span></div>
<div class="product-card" style="left:612px;top:2246px"><div class="product-name">Organic Spinach</div><div class="product-photo" role="img" aria-label="Spinach leaves" style="background:radial-gradient(circle,#2f6e1e 0%,#3f8a25 50%,#fff 78%)"></div><p class="product-text">Totam rem aperiam, eaque ipsa quae veritatis et quasi architecto...</p><div class="product-rating"><b>★★★★☆</b> 120 Reviews</div><span class="order-btn">Order Now</span></div>
<div class="product-card" style="left:868px;top:2246px"><div class="product-name">Organic Carrot</div><div class="product-photo" role="img" aria-label="Carrots with green tops" style="background:radial-gradient(circle,#e0692a 0%,#d2581e 35%,#fff 72%)"></div><p class="product-text">Totam rem aperiam, eaque ipsa quae veritatis et quasi architecto...</p><div class="product-rating"><b>★★★★☆</b> 120 Reviews</div><span class="order-btn">Order Now</span></div>

<footer class="site-footer">
  <div class="footer-brand"><span class="brand-dot"></span><span class="brand-name">Cultured Basics</span></div>
  <div class="social"><span></span><span></span><span></span><span></span><span></span></div>

  <div class="footer-col quick-links">
    <h3>Quick Link</h3>
    <ul><li>Home</li><li>Story</li><li>Product</li><li>How to take Cultured Basics</li><li>FAQ</li><li>Science Advisory Board</li></ul>
  </div>

  <div class="footer-col contact">
    <h3>Contact us</h3>
    <div class="contact-row"><svg width="12" height="16" viewBox="0 0 12 16"><path d="M6 0a6 6 0 0 1 6 6c0 4-6 10-6 10S0 10 0 6a6 6 0 0 1 6-6z" fill="#eee"/><circle cx="6" cy="6" r="2.2" fill="#1c1f1d"/></svg><span>P.O Box 1472<br>Marlow Bay Qld 4310</span></div>
    <div class="contact-row"><svg width="14" height="14" viewBox="0 0 14 14"><path d="M3 0l3 3-2 2c1 2 3 4 5 5l2-2 3 3-2 3C6 14 0 8 0 3z" fill="#eee"/></svg><span>Help : (07) 5550 1290</span></div>
    <div class="contact-row"><svg width="14" height="12" viewBox="0 0 14 12"><rect x="0" y="1" width="14" height="10" fill="#eee"/><path d="M0 1l7 6 7-6" stroke="#1c1f1d" stroke-width="1.4" fill="none"/></svg><span>info@culturedbasics.example</span></div>
  </div>

  <div class="contact-form">
    <div class="field" style="left:0;top:0;width:224px">Name</div>
    <div class="field" style="left:239px;top:0;width:224px">Mail</div>
    <div class="field" style="left:0;top:44px;width:224px">Phone</div>
    <div class="field" style="left:239px;top:44px;width:224px">Subject</div>
    <div class="field" style="left:0;top:86px;width:463px;height:64px">Message</div>
    <div class="send-btn">SEND MESSAGE</div>
  </div>
</footer>
<div class="footer-bar">© 2016 Cultured Basics.All Rights Reserved.</div>

</body>
</html>
```